Software Specialist in Artificial Intelligence innovation needs a smart and professional looking bus

Prefers a clean and professional design, yet portraying a class of its own and a world-class feel. We develop state-of-the-art software automation engines by deploying artificial intelligence that simulates the smartest brains that are able to simulate a human consultant and/or data scientist. Both single-sided or double-sided design is acceptable. Do not refer too much to our current website as we are also in the process of revamping it so that it better reflects who we are and what we do.
Updates

Project Deadline Extended
Reason: A substantial number of designs submitted to date deviates a fair bit from requirements and expectations. Feedbacks will be provided to all parties by today and as such, an extension is catered to accomodate re-submissions.

Target Market(s)

Software technology companies, software developers, enterprise clients that requires automation supported by Artificial Intelligence driven software solutions.

Industry/Entity Type

Software

Contact Information for Business Card

Marlo Vance
Chief Innovator
marlovance@brightquill.example
mobile: +65 94417302
Company Name: BrightQuill Pte Ltd
Address: 14 Tessaly Road #03-11 Harrow Court, Singapore 539204
Telephone: +65 63175420
Website: www.BrightQuill.example
Please do not include the titles of the above fields.

Font styles to use
Sans Serif
Other font styles liked:
• Calibri, Futura Condensed

Requirements
Must have
• Portrays a professional and innovative image. Should reflect that the company is into Artificial Intelligence software development, high tech kind of feel.
Nice to have
• A plus point would be if you can even come up with a new company logo for us, representing who we are. Our current company logo is attached.
Should not have
• Fanciful stuffs as it must portray a professional image. Prefers not to have the cloud "image" as part of the logo or in the name card.

```html
<!DOCTYPE html>
<html lang="en">
<head>
<meta charset="utf-8">
<title>BrightQuill Business Card</title>
<link href="https://fonts.googleapis.com/css2?family=Carlito:wght@400;700&display=swap" rel="stylesheet">
<style>
  :root {
    --backdrop: #e9e9ea;
    --brand-red: #b8323c;
    --ink: #262626;
    --paper: #f4f4f5;
    --white: #ffffff;
  }
  * { margin: 0; padding: 0; box-sizing: border-box; }
  html, body {
    width: 1200px; height: 900px; overflow: hidden;
    background: var(--backdrop);
    font-family: "Carlito", "Calibri", sans-serif;
  }
  .canvas { position: relative; width: 1200px; height: 900px; }

  .card {
    position: absolute;
    width: 620px; height: 350px;
    box-shadow: 0 6px 18px rgba(0,0,0,0.12);
    overflow: hidden;
  }

  .brand-name {
    display: block;
    font-weight: 700; font-size: 84px; line-height: 1;
    color: var(--ink); letter-spacing: -1px;
    white-space: nowrap;
  }
  .tagline {
    font-weight: 700; font-size: 27px; color: var(--ink);
    letter-spacing: 0.3px; white-space: nowrap;
  }

  /* Front */
  .card-front { left: 60px; top: 90px; background: var(--brand-red); }
  .card-front .brand-name { position: absolute; left: 52px; top: 118px; }
  .card-front .tagline { position: absolute; left: 56px; top: 212px; }

  /* Back */
  .card-back { left: 520px; top: 470px; background: var(--paper); }
  .card-back .brand-name { position: absolute; left: 44px; top: 36px; font-size: 68px; }
  .card-back .tagline { position: absolute; left: 46px; top: 112px; font-size: 23px; }

  .contact-band {
    position: absolute; left: 0; right: 0; bottom: 0; height: 182px;
    background: var(--brand-red);
    border-top: 6px solid var(--ink);
    color: var(--white);
    display: flex; justify-content: space-between;
    padding: 16px 30px 0 34px;
  }
  .contact-person .name-line {
    font-weight: 700; font-size: 24px; line-height: 1.2;
    margin-bottom: 6px; white-space: nowrap;
  }
  .contact-line { font-size: 14px; line-height: 1.4; white-space: nowrap; }
  .contact-office { padding-top: 6px; }
  .contact-office .contact-line { font-weight: 700; font-size: 15px; line-height: 1.7; }
</style>
</head>
<body>
<main class="canvas">

  <section class="card card-front" aria-label="Card front">
    <span class="brand-name">BrightQuill</span>
    <p class="tagline">Engineering the next Enterprise Mind</p>
  </section>

  <section class="card card-back" aria-label="Card back">
    <span class="brand-name">BrightQuill</span>
    <p class="tagline">Engineering the next Enterprise Mind</p>

    <div class="contact-band">
      <div class="contact-person">
        <p class="name-line">Marlo Vance Chief Innovator</p>
        <p class="contact-line">marlovance@brightquill.example</p>
        <p class="contact-line">Mobile: +65 94417302</p>
        <p class="contact-line">BrightQuill Pte Ltd</p>
        <p class="contact-line">14 Tessaly Road #03-11</p>
        <p class="contact-line">Harrow Court, Singapore 539204</p>
      </div>
      <div class="contact-office">
        <p class="contact-line">Telephone: +65 63175420</p>
        <p class="contact-line">Website: www.BrightQuill.example</p>
      </div>
    </div>
  </section>

</main>
</body>
</html>
```